Motor Vault Website - Part of the Brantley Group

A complimentary website is required for the launch of a 'Motor Vault' - a new service launched by industry renowned BRANTLEY. Motor Vault is an industry-first brand that designs and builds unique subterranean car parks for private residential homes in London and the influential counties within the UK. Please see here the direction of a new BRANTLEY Website - we would like Motor Vault to be complimentary and sit alongside BRANTLEY harmoniously - https://www.brantleyhq.example/brantley-nu-staging Brantley have some images, but whilst more professional images are in production - we have also attached pixmoor photos- named clearly as pixmoor. **Attached files include JPEG, .eps of logo and Brantley library images and Pixmoor Library Images - two versions of logo dependent on background colour. - Website needs to be sleek, chic and masculine.- Colour Palette - Grey/ Black/ White - Same visiual journey as Brantley website- Required areas within the sit include - About Us / Our Work / Contact Page

Target Market(s)

Luxury
Men

Number of Pages Required

2 page

Font styles to use
Sans Serif

Colors
e8e8e8
757575
1b1b1b
000000
9d9d9d
cbcbcb
f5f5f5

Requirements
Must have
• Complimentary of this site - https://www.brantleyhq.example/brantley-nu-staging
Should not have
• Colour

```html
<!DOCTYPE html>
<html lang="en">
<head>
<meta charset="utf-8">
<title>Motor Vault — Part of the Brantley Group</title>
<link href="https://fonts.googleapis.com/css2?family=Libre+Baskerville&family=Montserrat:wght@400;500&family=Work+Sans:wght@400&display=swap" rel="stylesheet">
<style>
  :root {
    --black: #000000;
    --ink: #1b1b1b;
    --grey-dark: #757575;
    --grey-mid: #9d9d9d;
    --grey-soft: #cbcbcb;
    --grey-light: #e8e8e8;
    --paper: #f5f5f5;
    --white: #ffffff;
  }
  * { box-sizing: border-box; margin: 0; padding: 0; }
  html, body { width: 730px; height: 1200px; overflow: hidden; background: var(--white); }
  body { font-family: 'Work Sans', sans-serif; color: var(--ink); }
  h1, h2 { font-weight: 400; }
  .page { position: relative; width: 730px; height: 1200px; overflow: hidden; }

  /* Header */
  .site-nav {
    position: absolute; top: 0; left: 0; width: 730px; height: 36px;
    background: var(--black); border-bottom: 1px solid #3a3a3a; z-index: 2;
  }
  .site-nav a {
    position: absolute; top: 14px; transform: translateX(-50%);
    font-family: 'Montserrat', sans-serif; font-size: 6.5px; letter-spacing: .3px;
    color: var(--grey-mid); text-decoration: none;
  }
  .site-nav a.is-home { color: var(--white); font-weight: 500; }
  .site-nav a.is-active { color: var(--white); }
  .site-nav .nav-underline {
    position: absolute; left: 370px; top: 34px; width: 60px; height: 2px; background: var(--grey-dark);
  }

  .hero {
    position: absolute; top: 0; left: 0; width: 730px; height: 368px;
    background: radial-gradient(ellipse at 50% 65%, #6a6a6a 0%, #2e2e2e 35%, #0a0a0a 70%, #000 100%);
  }
  .brand { position: absolute; text-align: right; }
  .brand-name {
    display: flex; align-items: center; gap: 6px;
    font-family: 'Montserrat', sans-serif; font-weight: 500; color: var(--white); line-height: 1;
  }
  .brand-mark { background: var(--white); display: inline-block; }
  .brand-tag {
    font-family: 'Montserrat', sans-serif; color: var(--grey-mid); letter-spacing: .2px; margin-top: 2px;
  }
  .hero-brand { left: 250px; top: 100px; z-index: 1; }
  .hero-brand .brand-name { font-size: 29px; }
  .hero-brand .brand-mark { width: 22px; height: 22px; }
  .hero-brand .brand-tag { font-size: 5px; }

  /* Intro */
  .intro { position: absolute; top: 368px; left: 0; width: 730px; text-align: center; }
  .intro-title {
    margin-top: 36px; font-family: 'Libre Baskerville', serif;
    font-size: 17.5px; color: #2b2b2b; letter-spacing: .3px;
  }
  .intro-text { margin-top: 9px; font-size: 7.5px; color: var(--grey-dark); }

  .features {
    position: absolute; top: 458px; left: 0; width: 730px; height: 210px; background: #f0f0f0;
  }
  .feature { position: absolute; top: 0; }
  .feature-title {
    height: 28px; line-height: 31px; text-align: center;
    font-family: 'Libre Baskerville', serif; font-size: 7px; letter-spacing: .6px; color: #2b2b2b;
  }
  .feature-image { height: 107px; }
  .feature-text {
    margin-top: 9px; padding: 0 8px; font-size: 6.3px; line-height: 10px; letter-spacing: .45px; color: var(--grey-dark);
  }

  /* Group slider */
  .group {
    position: absolute; top: 706px; left: 0; width: 730px; height: 350px;
    background: linear-gradient(100deg, #1e1e1e 0%, #3c3c3c 40%, #4a4a4a 60%, #262626 100%);
  }
  .group-title {
    position: absolute; top: 84px; width: 730px; text-align: center;
    font-family: 'Libre Baskerville', serif; font-size: 11px; letter-spacing: 1px; color: var(--white);
  }
  .group-rule { position: absolute; left: 323px; top: 116px; width: 83px; height: 2px; background: var(--white); }
  .group-copy {
    position: absolute; left: 144px; top: 137px; width: 444px;
    font-size: 6.3px; font-weight: 400; line-height: 9.8px; letter-spacing: .35px; color: var(--grey-light);
  }
  .group-copy p + p { margin-top: 10px; }
  .slider-arrow { position: absolute; top: 187px; }
  .slider-dots { position: absolute; top: 298px; left: 346px; display: flex; gap: 7px; }
  .slider-dots span { width: 8px; height: 8px; border-radius: 50%; border: 1px solid var(--grey-soft); }
  .slider-dots span.is-current { background: var(--grey-mid); border-color: var(--grey-mid); }

  /* Footer */
  .site-footer { position: absolute; top: 1056px; left: 0; width: 730px; height: 144px; background: var(--ink); }
  .site-footer .brand { left: 212px; top: 30px; }
  .site-footer .brand-name { font-size: 19px; gap: 4px; }
  .site-footer .brand-mark { width: 14px; height: 14px; }
  .site-footer .brand-tag { font-size: 3.6px; }
  .social { position: absolute; left: 213px; top: 65px; display: flex; gap: 20px; }
  .social span { width: 14px; height: 14px; background: var(--grey-dark); }
  .social span.is-hover { background: var(--white); }
  .footer-address {
    position: absolute; left: 212px; top: 93px; font-family: 'Montserrat', sans-serif;
    font-size: 5px; color: var(--grey-dark); letter-spacing: .2px;
  }
  .footer-links {
    position: absolute; left: 457px; top: 29px; width: 120px; list-style: none; text-align: center;
    font-family: 'Montserrat', sans-serif; font-size: 5.5px; line-height: 10px; color: var(--grey-soft);
  }
  .footer-links li.is-active { color: var(--white); text-decoration: underline; }
  .copyright {
    position: absolute; top: 120px; width: 730px; left: -10px; text-align: center;
    font-family: 'Montserrat', sans-serif; font-size: 5px; color: var(--grey-dark);
  }
  .copyright strong { font-weight: 400; color: var(--grey-soft); }
  .back-to-top { position: absolute; left: 578px; top: 116px; width: 15px; height: 15px; }
</style>
</head>
<body>
<div class="page">

  <section class="hero" role="img" aria-label="Covered classic car parked in a dark underground garage bay"></section>

  <nav class="site-nav">
    <a class="is-home" href="#" style="left:228px">HOME</a>
    <a href="#" style="left:311px">ABOUT</a>
    <a class="is-active" href="#" style="left:399px">CONTACT</a>
    <a href="#" style="left:494px">OUR WORK</a>
    <span class="nav-underline"></span>
  </nav>

  <div class="brand hero-brand">
    <div class="brand-name"><span class="brand-mark"></span>MOTOR VAULT</div>
    <div class="brand-tag">PART OF THE BRANTLEY GROUP</div>
  </div>

  <section class="intro">
    <h1 class="intro-title">FIRST-EVER. UNIQUE. PRIVATE.</h1>
    <p class="intro-text">We design and build a unique subterranean Car Parks for private residences in London and the Home Countries</p>
  </section>

  <section class="features">
    <article class="feature" style="left:137px;width:148px">
      <h2 class="feature-title">UNPARALLELED PROPOSITION</h2>
      <div class="feature-image" role="img" aria-label="Sunlight falling through a window into a bare concrete room" style="background:linear-gradient(135deg,#3a3a3a,#b0b0b0 45%,#2a2a2a)"></div>
      <p class="feature-text">Fusce non semper ante, sed aliquet lorem. Mauris elit urna, iaculis ac lacus a, vehicula luctus nisl. Donec interdum, mi vel dignissim sagittis, lectus felis egestas mi, ut aliquam neque felis in ipsum.</p>
    </article>
    <article class="feature" style="left:293px;width:144px">
      <h2 class="feature-title">EXCLUSIVE APPROACH</h2>
      <div class="feature-image" role="img" aria-label="Long dark concrete tunnel with a lit opening at the end" style="background:radial-gradient(circle at 50% 75%,#8a8a8a 0%,#2c2c2c 30%,#111 70%)"></div>
      <p class="feature-text">Nulla facilisi. In ultricies commodo ornare. Quisque a hendrerit augue. Donec mollis nisl nunc. Vivamus imperdiet, erat in dapibus fringilla, sem enim faucibus lorem, vel placerat purus lacus sed ex.</p>
    </article>
    <article class="feature" style="left:445px;width:148px">
      <h2 class="feature-title">EXPERIENCED TEAM</h2>
      <div class="feature-image" role="img" aria-label="Welder at work among steel reinforcement bars with sparks" style="background:linear-gradient(150deg,#1a1a1a,#6e6e6e 50%,#cfcfcf 75%,#2a2a2a)"></div>
      <p class="feature-text">Pellentesque accumsan ligula dolor, vitae molestie ipsum tempus et. Aenean ac magna in augue feugiat gravida. Cras et congue lectus. Etiam magna nisl, aliquet id eros vel, faucibus dignissim ante.</p>
    </article>
  </section>

  <section class="group" aria-label="Modern brick and timber lounge interior with leather seating">
    <h2 class="group-title">PART OF THE BRANTLEY GROUP</h2>
    <span class="group-rule"></span>
    <div class="group-copy">
      <p>Lorem ipsum dolor sit amet, consectetur adipiscing elit. Aliquam posuere molestie diam, eget egestas dolor. Aenean elit erat, euismod vel dui a, sollicitudin commodo urna. Integer rutrum dictum metus a viverra. Sed vulputate purus vel pulvinar blandit. Cras ac lorem tincidunt, ullamcorper purus quis, blandit dui. Vestibulum ante ipsum primis in faucibus orci luctus et ultrices posuere cubilia Curae; Vivamus ligula eros, mollis vel magna non, auctor maximus libero. In sit amet lacus a felis fermentum aliquet eu at ex. Mauris at libero dictum, tincidunt augue laoreet, maximus massa.</p>
      <p>Proin eleifend nec lacus ut volutpat. Proin non augue commodo, vulputate metus id, cursus risus. Nulla tincidunt nunc purus. Donec ac lorem vel tellus volutpat semper at non arcu. Vestibulum nec molestie mi. Sed a leo sapien. Vestibulum ultrices dictum elit ut auctor.</p>
      <p>Curabitur ac lectus varius, aliquet urna in, gravida leo. In quis nunc urna. Vestibulum porta pulvinar tincidunt. Vestibulum aliquet cursus lorem et suscipit. Donec id sollicitudin odio, sed accumsan est. Aenean feugiat elit a libero ullamcorper varius. Duis elementum turpis erat, ac vestibulum eros pulvinar nec. Maecenas eget eros augue.</p>
    </div>
    <svg class="slider-arrow" style="left:63px" width="18" height="30" viewBox="0 0 18 30"><polyline points="15,2 3,15 15,28" fill="none" stroke="#9d9d9d" stroke-width="3"/></svg>
    <svg class="slider-arrow" style="left:650px" width="18" height="30" viewBox="0 0 18 30"><polyline points="3,2 15,15 3,28" fill="none" stroke="#9d9d9d" stroke-width="3"/></svg>
    <div class="slider-dots"><span class="is-current"></span><span></span><span></span></div>
  </section>

  <footer class="site-footer">
    <div class="brand">
      <div class="brand-name"><span class="brand-mark"></span>MOTOR VAULT</div>
      <div class="brand-tag">PART OF THE BRANTLEY GROUP</div>
    </div>
    <div class="social"><span></span><span></span><span></span><span class="is-hover"></span><span></span></div>
    <p class="footer-address">001 HARROW MEWS, LONDON, W9 4QT | TEL: 0200 555 XXX</p>
    <ul class="footer-links">
      <li>HOME</li>
      <li class="is-active">ABOUT</li>
      <li>OUR WORK</li>
      <li>CONTACT</li>
      <li>TERMS &amp; CONDITIONS</li>
      <li>PRIVACY POLICY</li>
    </ul>
    <p class="copyright">Copyright © <strong>MOTOR VAULT</strong> 2019</p>
    <svg class="back-to-top" viewBox="0 0 15 15"><rect width="15" height="15" fill="#3a3a3a"/><path d="M7.5 3 L12 8 H9 V12 H6 V8 H3 Z" fill="#1b1b1b"/></svg>
  </footer>

</div>
</body>
</html>
```